Newspaper Ad for Cool Hawaiian PPE Company

We need an incredible ad for our local newspaper to tell everyone about BreezeGuard.com. We want a beautiful ad that is sophisticated with a local flair. Less is more. Clean. Stands out. We are safely shipping masks and PPE to our local community. Everyone has access to the supplies they need to keep them and their loved ones safe during the pandemic. Make it really pop.

Target Market(s)

Community members

Requirements
Must have
• Half Page:

Specs 9.7” x 10” column inches for the half page. Minimum 300 dpi, jpeg is fine.

```html
<!DOCTYPE html>
<html lang="en">
<head>
<meta charset="utf-8">
<title>BreezeGuard.com – Newspaper Ad</title>
<link rel="stylesheet" href="https://fonts.googleapis.com/css2?family=Arimo:ital,wght@1,700&family=Barlow:ital,wght@1,400&display=swap">
<style>
  :root {
    --paper: #ffffff;
    --leaf-green: #1f8a3b;
    --brand-grey: #5e5e5e;
    --ocean: #2f6f8a;
    --headline: #ffffff;
    --frame-white: #f4f7f8;
  }
  html, body {
    margin: 0;
    padding: 0;
    overflow: hidden;
    background: var(--paper);
  }
  .ad {
    position: relative;
    width: 1162px;
    height: 1200px;
    overflow: hidden;
    background: var(--paper);
  }
  .brand {
    position: absolute;
    left: 70px;
    top: 118px;
    display: flex;
    align-items: center;
    gap: 14px;
  }
  .brand__dot {
    width: 26px;
    height: 26px;
    border-radius: 50%;
    background: var(--leaf-green);
  }
  .brand__name {
    font-family: "Arimo", Arial, sans-serif;
    font-weight: 700;
    font-style: italic;
    font-size: 38px;
    color: var(--brand-grey);
    letter-spacing: -0.5px;
  }
  .tagline {
    position: absolute;
    left: 40px;
    width: 400px;
    top: 318px;
    margin: 0;
    font-family: "Barlow", Arial, sans-serif;
    font-style: italic;
    font-weight: 400;
    font-size: 33px;
    line-height: 48.5px;
    text-align: center;
    color: var(--leaf-green);
  }
  .frame-green-top {
    position: absolute;
    left: 481px;
    top: 68px;
    width: 594px;
    height: 5px;
    background: var(--leaf-green);
  }
  .frame-green-side {
    position: absolute;
    left: 479px;
    top: 68px;
    width: 5px;
    height: 404px;
    background: var(--leaf-green);
  }
  .photo {
    position: absolute;
    left: 518px;
    top: 105px;
    width: 644px;
    height: 949px;
    background: linear-gradient(180deg,
      #c9ccc4 0%, #e9e7e0 14%, #f3f1ec 26%,
      #b8a596 40%, #8f8a86 55%, #a59ea0 68%,
      #c86a78 80%, #d9a23c 92%, #c9871f 100%);
  }
  .panel {
    position: absolute;
    left: 0;
    top: 576px;
    width: 518px;
    height: 624px;
    background: var(--ocean);
  }
  .band {
    position: absolute;
    left: 0;
    top: 1054px;
    width: 1162px;
    height: 146px;
    background: var(--ocean);
  }
  .frame-white-side {
    position: absolute;
    left: 481px;
    top: 673px;
    width: 3px;
    height: 424px;
    background: var(--frame-white);
  }
  .frame-white-bottom {
    position: absolute;
    left: 481px;
    top: 1094px;
    width: 440px;
    height: 3px;
    background: var(--frame-white);
  }
  .web {
    position: absolute;
    left: 938px;
    top: 1079px;
    font-family: "Barlow", Arial, sans-serif;
    font-style: normal;
    font-size: 26px;
    line-height: 32px;
    color: var(--frame-white);
  }
  .headline {
    margin: 0;
  }
  .headline span {
    position: absolute;
    left: 0;
    width: 480px;
    text-align: center;
    font-family: "Arimo", Arial, sans-serif;
    font-weight: 700;
    font-style: italic;
    line-height: 1;
    color: var(--headline);
    letter-spacing: -1px;
    white-space: nowrap;
  }
  .headline .l-keep   { top: 654px;  font-size: 58px; }
  .headline .l-and    { top: 714px;  font-size: 42px; }
  .headline .l-loved  { top: 749px;  font-size: 73px; }
  .headline .l-ones   { top: 814px;  font-size: 73px; }
  .headline .l-safe   { top: 874px;  font-size: 108px; letter-spacing: -2px; }
  .headline .l-during { top: 999px;  font-size: 42px; }
  .headline .l-pandemic { top: 1039px; font-size: 70px; }
</style>
</head>
<body>
<main class="ad">
  <div class="brand">
    <span class="brand__dot"></span>
    <span class="brand__name">BreezeGuard.com</span>
  </div>

  <p class="tagline">WE ARE SAFELY<br>SHIPPING MASKS<br>AND PPE TO OUR<br>LOCAL COMMUNITY</p>

  <div class="frame-green-top"></div>
  <div class="frame-green-side"></div>

  <div class="photo" role="img" aria-label="Photo of a young girl in a patterned face mask at an outdoor farmers market, holding a dragon fruit above a table of yellow fruit"></div>

  <div class="panel"></div>
  <div class="band"></div>

  <h1 class="headline">
    <span class="l-keep">KEEP THEM</span>
    <span class="l-and">AND THEIR</span>
    <span class="l-loved">LOVED</span>
    <span class="l-ones">ONES</span>
    <span class="l-safe">SAFE</span>
    <span class="l-during">DURING THE</span>
    <span class="l-pandemic">PANDEMIC</span>
  </h1>

  <div class="frame-white-side"></div>
  <div class="frame-white-bottom"></div>
  <div class="web">BreezeGuard.com</div>
</main>
</body>
</html>
```